Brand new website for global research and investment startup

We need a simple website, maybe 3 pages: landing page with business description, investment philosophy, team and contact info.
We have a logo already that can be incorporated. Please use the logo only, not the text
We like the color green, something along the lines of #3D6C32 as the main color.
We'd like to design the website with geometric shapes in gradations of the base color. The shapes should suggest "work in progress", "built to last (a long time)", "solidity" and "indestructibility". One idea floating in my head sees smaller features with icosahedron and dodecahedron shapes, and maybe larger structures like crystal lattices; but please feel free to be creative and imagine your own.

```html
<!DOCTYPE html>
<html lang="en">
<head>
<meta charset="UTF-8">
<title>Halvard Meridian | Global Research &amp; Investment Firm</title>
<link href="https://fonts.googleapis.com/css2?family=Cormorant+Garamond:wght@500;600&family=Roboto:wght@400;500;700&display=swap" rel="stylesheet">
<style>
:root{
  --forest:#0f4a0a;
  --forest-deep:#0b3d08;
  --brand:#3d6c32;
  --brand-btn:#2f6a2a;
  --accent:#5fd35a;
  --paper:#eceee2;
  --paper-alt:#e7eadd;
  --ink:#1d2a17;
  --text:#3a4236;
  --muted:#6b7266;
  --line:#c9cdbf;
  --white:#ffffff;
}
*{box-sizing:border-box;margin:0;padding:0}
html,body{width:1200px;height:2908px;overflow:hidden}
body{background:var(--paper);font-family:'Roboto',sans-serif;color:var(--text);font-size:13px;line-height:1.45}
.serif{font-family:'Cormorant Garamond',serif}
a{color:inherit;text-decoration:none}

/* header */
.site-header{height:74px;background:var(--forest);display:flex;align-items:center;padding:0 47px 0 60px}
.brand-name{font-family:'Cormorant Garamond',serif;font-weight:600;font-size:24px;color:var(--white);letter-spacing:.5px}
.main-nav{margin-left:auto;display:flex;align-items:center;height:100%}
.main-nav a{font-family:'Cormorant Garamond',serif;font-weight:600;font-size:13px;color:var(--white);padding:0 16px;border-right:1.5px solid var(--white);line-height:30px}
.main-nav a:last-child{border-right:0}
.main-nav a.active{color:var(--accent);border-bottom:3px solid var(--accent)}
.btn-outline{margin-left:110px;border:2px solid var(--white);border-radius:4px;color:var(--white);font-family:'Cormorant Garamond',serif;font-weight:600;font-size:13px;padding:6px 18px}

/* hero */
.hero{position:relative;height:552px;background:linear-gradient(90deg,var(--forest-deep) 0%,#0c5210 45%,#126a20 70%,#1a7a2c 100%);overflow:hidden}
.hero-visual{position:absolute;right:0;top:0;width:720px;height:552px;background:radial-gradient(ellipse at 70% 40%,#2e9a45 0%,#17702a 40%,rgba(12,82,16,0) 75%)}
.hero-copy{position:absolute;left:47px;top:125px;width:440px;color:var(--white)}
.hero-copy h1{font-family:'Cormorant Garamond',serif;font-weight:500;font-size:52px;line-height:1.02}
.hero-copy p{margin-top:20px;border-left:1.5px solid var(--white);padding:6px 0 6px 8px;font-size:12.5px;line-height:1.55}
.btn-solid{display:inline-flex;align-items:center;gap:6px;background:var(--brand);color:var(--white);font-family:'Cormorant Garamond',serif;font-weight:600;font-size:12.5px;padding:7px 18px;border-radius:2px}
.hero-copy .btn-solid{margin-top:18px}

/* sections */
.section{position:relative}
.intro{height:427px;padding-top:44px;text-align:center}
.section-title{font-family:'Cormorant Garamond',serif;font-weight:600;font-size:36px;color:var(--ink);line-height:1.1}
.section-sub{font-family:'Cormorant Garamond',serif;font-weight:500;font-size:19px;color:var(--ink);margin-top:10px}
.prose{width:580px;margin:0 auto;text-align:justify;font-size:12.5px;line-height:1.55}
.prose p{margin-top:11px}
.intro .prose{margin-top:22px}
.prose strong{color:var(--ink)}
.eyebrow{font-size:11px;font-weight:500;color:var(--brand);text-transform:uppercase;letter-spacing:.3px}

.philosophy{height:365px;padding-top:56px;text-align:center}
.philosophy .section-title{margin-top:12px;font-size:35px}
.cards{display:flex;justify-content:center;gap:17px;margin-top:18px}
.card{width:194px;height:158px;border:2px solid var(--brand);border-radius:3px;padding:8px 8px;text-align:center}
.card svg{display:block;margin:0 auto}
.card h3{font-size:17px;font-weight:500;color:var(--brand-btn);margin-top:14px}
.card p{font-size:12px;color:var(--muted);margin-top:8px;line-height:1.55}

.team{height:348px;background:var(--paper-alt);padding:56px 0 0 47px;display:flex}
.team-intro{width:400px}
.team-intro h2{font-family:'Cormorant Garamond',serif;font-weight:600;font-size:35px;color:var(--ink);line-height:1;margin-top:12px}
.team-intro p{border-left:1.5px solid var(--muted);padding:3px 0 3px 8px;margin-top:18px;font-size:12.5px;line-height:1.55}
.team-intro .btn-solid{margin-top:22px;border:2px solid var(--brand-btn);background:var(--brand-btn)}
.members{display:flex;margin-left:84px;margin-top:4px}
.member{width:162px;height:222px;text-align:center;border-right:1.5px solid var(--brand)}
.member:last-child{border-right:0}
.avatar{width:108px;height:108px;border-radius:50%;background:#a0a0a0;margin:0 auto}
.member h4{font-size:12.5px;font-weight:500;color:var(--ink);margin-top:24px}
.member span{display:block;font-size:11px;color:var(--muted);margin-top:12px}
.social{display:flex;justify-content:center;gap:24px;margin-top:14px}
.social i{width:19px;height:19px;background:var(--brand);border-radius:2px}

.research{height:497px;padding-top:54px;text-align:center}
.research .section-title{margin-top:12px;font-size:35px}
.research .lede{width:510px;margin:40px auto 0;text-align:left;font-size:12.5px;line-height:1.55}
.research .prose{margin-top:0}

.contact{height:371px;display:flex;padding:50px 47px 0}
.contact-head{width:340px;padding-top:86px}
.contact-head h2{font-family:'Cormorant Garamond',serif;font-weight:600;font-size:35px;color:var(--ink);line-height:1.05;margin-top:14px}
.contact-info{width:380px;border-left:1.5px solid var(--brand);padding:0 0 0 18px;height:277px}
.info-row{display:flex;gap:12px;align-items:flex-start;font-size:12px;padding:10px 0 6px;border-bottom:1px solid var(--line)}
.info-row:last-of-type{border-bottom:0}
.map-area{width:360px;height:120px;margin-top:6px;background:linear-gradient(135deg,#dfe3ea,#c9d0dc)}
.contact-form{width:360px;margin-left:20px;display:grid;grid-template-columns:1fr 1fr;column-gap:8px;row-gap:4px;align-content:start}
.field label{display:block;font-size:11.5px;color:var(--muted)}
.field .input{height:30px;border:1.5px solid #b8bcb2;background:var(--white);font-size:11px;color:#9aa096;padding:6px 12px}
.field.full{grid-column:1/3}
.field .textarea{height:74px}
.btn-submit{grid-column:1/3;margin-top:6px;height:30px;background:var(--brand-btn);color:var(--white);font-size:12px;font-weight:700;display:flex;align-items:center;justify-content:center;gap:5px;border-radius:3px}

.site-footer{height:274px;background:var(--forest);padding:0 38px;color:var(--white)}
.footer-top{height:132px;display:flex;align-items:center;border-bottom:1px solid #7e9a78;padding-top:18px}
.footer-top .brand-name{width:290px;padding-left:80px}
.footer-nav{display:flex;flex:1}
.footer-nav a{flex:1;text-align:center;font-size:13px;border-right:1.5px solid var(--white);line-height:26px}
.footer-nav a:last-child{border-right:0}
.footer-nav a.active{color:var(--accent)}
.footer-bottom{display:flex;justify-content:space-between;padding:24px 12px 0 18px;font-size:12px}
.legal a{padding:0 8px;border-right:1px solid var(--white)}
.legal a:last-child{border-right:0;padding-right:0}
</style>
</head>
<body>

<header class="site-header">
  <span class="brand-name">Halvard Meridian</span>
  <nav class="main-nav">
    <a href="#" class="active">HOME</a>
    <a href="#">PHILOSOPHY</a>
    <a href="#">TEAM</a>
    <a href="#">CONTACT</a>
  </nav>
  <a href="#" class="btn-outline">INQUIRY FORM &#8594;</a>
</header>

<section class="hero">
  <div class="hero-visual" role="img" aria-label="Green geometric lattice network of connected nodes and lines"></div>
  <div class="hero-copy">
    <h1>Halvard Meridian | Global Research &amp; Investment Firm</h1>
    <p>Halvard Meridian is a global research and investment firm focused on long-term value, rigorous research, disciplined investing, and enduring opportunities.</p>
    <a href="#" class="btn-solid">CONTACT US NOW &#8594;</a>
  </div>
</section>

<section class="section intro">
  <h2 class="section-title">Global Insight. Enduring Value. Built To Last.</h2>
  <p class="section-sub">Investing with Purpose and Perspective</p>
  <div class="prose">
    <p>We are a global research and investment firm focused on identifying long-term value through clarity, conviction, and discipline.</p>
    <p>We combine rigorous research, independent thinking, and a global perspective to uncover opportunities with lasting potential. Our approach is grounded in fundamental analysis, thoughtful decision-making, and a deep understanding of the forces shaping markets and industries.</p>
    <p>We look beyond short-term market movements to identify businesses, ideas, and opportunities capable of creating sustainable value over time. With patience, discipline, and a commitment to long-term thinking, we build conviction around investments that we believe can endure.</p>
    <p>Our philosophy is simple: <strong>research deeply, think independently, act with discipline, and build for the long term.</strong></p>
  </div>
</section>

<section class="section philosophy">
  <p class="eyebrow">Our Philosophy</p>
  <h2 class="section-title">Investing With Purpose And Perspective.</h2>
  <div class="cards">
    <div class="card">
      <svg width="34" height="34" viewBox="0 0 34 34" fill="none" stroke="#3d6c32" stroke-width="2"><circle cx="17" cy="14" r="9"/><path d="M8 14h18M17 5c4 4 4 14 0 18M17 5c-4 4-4 14 0 18"/><path d="M6 28h22"/></svg>
      <h3>Global Perspective</h3>
      <p>We look beyond borders to find ideas that outperform over time.</p>
    </div>
    <div class="card">
      <svg width="38" height="34" viewBox="0 0 38 34" fill="none" stroke="#3d6c32" stroke-width="2"><rect x="3" y="4" width="30" height="20"/><path d="M8 20v-5M13 20v-8M18 20v-4"/><circle cx="26" cy="19" r="5"/><path d="M30 23l5 5M12 30h14"/></svg>
      <h3>Research-Driven</h3>
      <p>Deep analysis, original thinking, and rigorous due diligence.</p>
    </div>
    <div class="card">
      <svg width="36" height="34" viewBox="0 0 36 34" fill="#3d6c32"><path d="M10 6h10l-3 5c7 3 9 9 9 14 0 5-5 7-11 7S4 30 4 25c0-5 3-11 9-14z"/><circle cx="28" cy="26" r="6"/></svg>
      <h3>Long-Term Mindset</h3>
      <p>We invest for decades, not quarters, with patience and discipline.</p>
    </div>
    <div class="card">
      <svg width="34" height="34" viewBox="0 0 34 34" fill="#3d6c32"><rect x="9" y="14" width="4" height="10"/><rect x="15" y="9" width="4" height="15"/><rect x="21" y="4" width="4" height="20"/><path d="M4 24h8l6 4h12v3H4z"/></svg>
      <h3>Built To Last</h3>
      <p>Our approach is rooted in resilience, integrity, and impact.</p>
    </div>
  </div>
</section>

<section class="section team">
  <div class="team-intro">
    <p class="eyebrow">Our Team</p>
    <h2>Experienced. Independent. Aligned.</h2>
    <p>Our team brings together decades of experience in research, investing, and building enduring businesses.</p>
    <a href="#" class="btn-solid">MEET THE TEAM &#8594;</a>
  </div>
  <div class="members">
    <div class="member"><div class="avatar" role="img" aria-label="Team member portrait placeholder"></div><h4>Member Name</h4><span>Postion In Company</span><div class="social"><i></i><i></i></div></div>
    <div class="member"><div class="avatar" role="img" aria-label="Team member portrait placeholder"></div><h4>Member Name</h4><span>Postion In Company</span><div class="social"><i></i><i></i></div></div>
    <div class="member"><div class="avatar" role="img" aria-label="Team member portrait placeholder"></div><h4>Member Name</h4><span>Postion In Company</span><div class="social"><i></i><i></i></div></div>
    <div class="member"><div class="avatar" role="img" aria-label="Team member portrait placeholder"></div><h4>Member Name</h4><span>Postion In Company</span><div class="social"><i></i><i></i></div></div>
  </div>
</section>

<section class="section research">
  <p class="eyebrow">Research</p>
  <h2 class="section-title">Research-Driven Investment Approach</h2>
  <p class="lede">Deep analysis, original thinking, and rigorous due diligence guide every investment decision.</p>
  <div class="prose">
    <p>We believe strong investment decisions begin with <strong>strong research</strong>. Our process combines fundamental analysis, independent research, market intelligence, and a disciplined evaluation of risk and opportunity.</p>
    <p>We examine businesses, industries, markets, and broader economic trends to understand not only where an opportunity stands today, but where it could go over the long term.</p>
    <p>Our team challenges assumptions, examines evidence from multiple perspectives, and seeks to distinguish lasting value from short-term market noise. Every opportunity is assessed with patience, discipline, and a clear understanding of its underlying fundamentals.</p>
    <p>We do not invest simply because an opportunity is popular or timely. <strong>We invest when our research gives us conviction.</strong></p>
  </div>
</section>

<section class="section contact">
  <div class="contact-head">
    <p class="eyebrow">Contact Us</p>
    <h2>Let's Build The Future Together.</h2>
  </div>
  <div class="contact-info">
    <div class="info-row">
      <svg width="16" height="18" viewBox="0 0 16 18" fill="#3d6c32"><path d="M8 0a6 6 0 0 1 6 6c0 5-6 12-6 12S2 11 2 6a6 6 0 0 1 6-6z"/><circle cx="8" cy="6" r="2.2" fill="#eceee2"/></svg>
      <span>Global Headquarters 48 Meridian Row Northfield, NY 10099</span>
    </div>
    <div class="info-row">
      <svg width="18" height="14" viewBox="0 0 18 14" fill="#3d6c32"><rect width="18" height="14" rx="1"/><path d="M1 1l8 6 8-6" stroke="#eceee2" stroke-width="1.5" fill="none"/></svg>
      <span>info@halvardmeridian.example</span>
    </div>
    <div class="info-row">
      <svg width="18" height="16" viewBox="0 0 18 16" fill="#3d6c32"><path d="M1 4c0-2 3-3 8-3s8 1 8 3v2h-4V4H5v2H1z"/><rect x="3" y="7" width="12" height="8" rx="1"/></svg>
      <span>+1 (212) 555-0147</span>
    </div>
    <div class="map-area" role="img" aria-label="Street map showing the headquarters location"></div>
  </div>
  <form class="contact-form">
    <div class="field"><label>Name</label><div class="input">Name</div></div>
    <div class="field"><label>Email</label><div class="input">Email</div></div>
    <div class="field"><label>Phone</label><div class="input">Phone</div></div>
    <div class="field"><label>Subject</label><div class="input">Subject</div></div>
    <div class="field full"><label>Message</label><div class="input textarea">Message</div></div>
    <div class="btn-submit">SUBMITE &#8594;</div>
  </form>
</section>

<footer class="site-footer">
  <div class="footer-top">
    <span class="brand-name">Halvard Meridian</span>
    <nav class="footer-nav">
      <a href="#" class="active">HOME</a>
      <a href="#">PHILOSOPHY</a>
      <a href="#">TEAM</a>
      <a href="#">CONTACT</a>
    </nav>
  </div>
  <div class="footer-bottom">
    <span>&copy; 2026 Halvard Meridian. All rights reserved.</span>
    <span class="legal"><a href="#">Privacy Policy Profile</a><a href="#">Terms of Use</a><a href="#">Profile</a></span>
  </div>
</footer>

</body>
</html>
```